We need visit card and a letter paper for our website. thx

We have a beauty clinic in Switzerland.
https://wiesentalblick.ch
We need a visit card.

Requirements
Must have
• see colors on website

```html
<!DOCTYPE html>
<html lang="de">
<head>
<meta charset="utf-8">
<title>Wiesentalblick – Visitenkarte</title>
<link href="https://fonts.googleapis.com/css2?family=Lato:wght@300;400;700&display=swap" rel="stylesheet">
<style>
  :root {
    --stage: #1e1e1e;
    --card-dark: #151515;
    --card-dark-hi: #2e2e2e;
    --card-light: #ffffff;
    --ink: #111111;
    --ink-soft: #5a5a5a;
    --on-dark: #ffffff;
  }
  * { box-sizing: border-box; margin: 0; padding: 0; }
  html, body { width: 1200px; height: 852px; overflow: hidden; }
  body {
    background: var(--stage);
    font-family: "Lato", sans-serif;
    display: flex;
    flex-direction: column;
    align-items: center;
    justify-content: center;
    gap: 40px;
  }
  .card {
    position: relative;
    width: 620px;
    height: 354px;
    border-radius: 18px;
    overflow: hidden;
  }
  .card--back {
    background: radial-gradient(ellipse at 50% 20%, var(--card-dark-hi), var(--card-dark) 70%);
    display: flex;
    align-items: center;
    justify-content: center;
  }
  .brand {
    display: flex;
    align-items: center;
    gap: 12px;
    font-weight: 400;
    letter-spacing: 0.5px;
  }
  .brand__mark {
    width: 10px;
    height: 10px;
    border: 1.5px solid currentColor;
  }
  .card--back .brand { color: var(--on-dark); font-size: 44px; }
  .card--front { background: var(--card-light); color: var(--ink); }
  .card--front .brand {
    position: absolute;
    top: 62px;
    right: 44px;
    font-size: 30px;
    color: var(--ink);
  }
  .team {
    position: absolute;
    top: 66px;
    left: 48px;
    font-size: 15px;
    font-weight: 400;
    line-height: 1.4;
  }
  .contact {
    position: absolute;
    left: 48px;
    bottom: 40px;
    font-size: 14px;
    font-weight: 300;
    color: var(--ink-soft);
    line-height: 1.45;
  }
  .contact__address { margin-bottom: 12px; }
  .contact__line { display: flex; align-items: center; gap: 12px; }
  .contact__line svg { width: 11px; height: 11px; fill: var(--ink); flex: none; }
</style>
</head>
<body>
  <section class="card card--back">
    <div class="brand"><span class="brand__mark"></span>Wiesentalblick</div>
  </section>

  <section class="card card--front">
    <div class="team">
      <p>Dr. Lena Marti</p>
      <p>Dr. Tobias Huber, DESA</p>
    </div>
    <div class="brand"><span class="brand__mark"></span>Wiesentalblick</div>
    <div class="contact">
      <p class="contact__address">Bachweg 14, 8610<br>Uster, Switzerland</p>
      <p class="contact__line">
        <svg viewBox="0 0 12 12" aria-hidden="true"><path d="M2.5 1l2 2.2-1 1.3a7 7 0 0 0 4 4l1.3-1 2.2 2-1.2 1.5C5.5 11 1 6.5 1 2.2z"/></svg>
        +41 (0) 800 24 20 20
      </p>
      <p class="contact__line">
        <svg viewBox="0 0 12 12" aria-hidden="true"><path d="M1 2.5h10v7H1zm1.2 1L6 6.3l3.8-2.8H2.2zM2 4.5v4h8v-4L6 7.5z" fill-rule="evenodd"/></svg>
        hallo@wiesentalblick.ch
      </p>
      <p class="contact__line">
        <svg viewBox="0 0 12 12" aria-hidden="true"><path d="M6 1a5 5 0 1 0 0 10A5 5 0 0 0 6 1zm0 1c.7.8 1.1 2 1.2 3.4H4.8C4.9 4 5.3 2.8 6 2zm-1.9.4A6 6 0 0 0 3.8 5.4H2.1a4 4 0 0 1 2-3zm3.8 0a4 4 0 0 1 2 3H8.2a6 6 0 0 0-.3-3zM2.1 6.6h1.7c0 1.1.2 2.1.3 3a4 4 0 0 1-2-3zm2.7 0h2.4C7.1 8 6.7 9.2 6 10c-.7-.8-1.1-2-1.2-3.4zm3.4 0h1.7a4 4 0 0 1-2 3c.2-.9.3-1.9.3-3z" fill-rule="evenodd"/></svg>
        wiesentalblick.ch
      </p>
    </div>
  </section>
</body>
</html>
```